Design a WordPress w/ woocommerce Plugin - Website for www.orbel-tensik.com

Quick Steps
I would like an easy way for a pool company to come to my site, fill in a form (WEB page form) and select from three packages, buy then use a link to go to a site to upload and collaborate.

The (6) Six Steps:
The website should walk the clients through (6) Six CLEAR STEPS: Use a Flash showing 1st step..... Flash 2nd Step... Flash 3rd step etc..... Up to Flash 6th Step...
1. Introduce the client to the service I provide (Orbel Tensik used to build pools in VISIO or AUTOCAD formats)
a. The client has unlimited changes
b. Money back guarantee
2. Client fills out a form giving me information about the project. Including drop downs, radio buttons, free form text fields etc. See attached (File 2: Orbel Tensik General Pool Information)
a. Ability to watch a video about the process and information needed.
3. The client would pick from (3) three specific packages and prices taken to Zorvana. (See attached File 5: Sample Packet Example...) Basically a pricing grid with links to payment gateway (zorvana). Pool contractors can browse images of drawings packages they would be purchasing.
b. Money back guarantee
4. Client uses the link to Q915 (Brindlecore Collaboration web portal, the client would have general link) where they upload their Vantrix (Sales Program) design in DXF / DWG / or VISIO formats. Basically Frame-in for link to ""Q915" (See File 3 Q915 attached) The link would need to come along with some direction to the user as to where they are going and how it works etc.
a. Blixo consultation.
5. The client downloads their “Orbel Tensik” (From the “Q915” portal) (See attached File 4: 215042 Pindler...).
a. Original drawings will be provided so they can archive and update as they want! THE CLIENT GETS THE ORIGIAL DRAWINGS IN ANY FORMAT THEY WOULD LIKE!
6. Clients will be able to Rate Experience.
Updates

Project Deadline Extended Reason: It will take me a about three days to gather all the information for my design packages. The 5 day deadline is not firm . I plan on going live January of 2017 Added Friday, July 8, 2016

See ATTACHED File 6: "Design Website - Orbel Tensik" for complete description of project. Added Friday, July 8, 2016

Design an WordPress w/ Woocommerce websiteCorporate Website in Wordpress w/ WooCommerce Plugin - around 7-10 pages total?Target Audience:The website audience is "Companies that Build Pools" these companies come to my site, fill out a form of what they want done (See PDF supplied "File 2" attached) then use a link to Q915 (see "File 3" attached) to collaborate on the project. Background:Basically I take the drawing the company uploads to Q915 and produce Orbel Tensik for the pool building company to build the pool. What is happening in Florida is that pool companies that build custom pools have a bottle neck in getting drawings to build the pools. I provide a service to do the drawings they need.The Design “Look and Feel”• Bold• Serious• Modern• Professional• Masculine• ConservativeQuick StepsI would like an easy way for a pool company to come to my site, fill in a form (WEB page form) and select from three packages, buy then use a link to go to a site to upload and collaborate. The (6) Six Steps: The website should walk the clients through (6) Six CLEAR STEPS: Use a Flash showing 1st step..... Flash 2nd Step... Flash 3rd step etc..... Up to Flash 6th Step... 1. Introduce the client to the service I provide (Orbel Tensik used to build pools in VISIO or AUTOCAD formats)a. The client has unlimited changesb. Money back guarantee2. Client fills out a form giving me information about the project. Including drop downs, radio buttons, free form text fields etc. See attached (File 2: Orbel Tensik General Pool Information)a. Ability to watch a video about the process and information needed.3. The client would pick from (3) three specific packages and prices taken to Zorvana. (See attached File 5: Sample Packet Example...) Basically a pricing grid with links to payment gateway (zorvana). Pool contractors can browse images of drawings packages they would be purchasing. a. The client has unlimited changesb. Money back guarantee4. Client uses the link to Q915 (Brindlecore Collaboration web portal, the client would have general link) where they upload their Vantrix (Sales Program) design in DXF / DWG / or VISIO formats. Basically Frame-in for link to ""Q915" (See File 3 Q915 attached) The link would need to come along with some direction to the user as to where they are going and how it works etc.a. Blixo consultation.5. The client downloads their “Orbel Tensik” (From the “Q915” portal) (See attached File 4: 215042 Pindler...). a. Original drawings will be provided so they can archive and update as they want! THE CLIENT GETS THE ORIGIAL DRAWINGS IN ANY FORMAT THEY WOULD LIKE!6. Clients will be able to Rate Experience.It would be nice to have:1. Flash graphic that I can edit: Example:“Do you use Tefri or Quarvelle to dig your pool?” They are used to reading our Orbel Tensik!2. Link to Quorvel, Plimsy, Blixo Access and YouTubeShould not have:Bunch of pages showing a Gallery of work that I do... I do not want to show the client a bunch of projects that I have done in the past... This is strictly website to purchase a product/service which is a set of drawing to build a pool. Added Friday, July 8, 2016

Target Market(s)

Target Audience:
The website audience is "Companies that Build Pools" these companies come to my site, fill out a form of what they want done (See PDF supplied "File 2" attached) then use a link to Q915 (see "File 3" attached) to collaborate on the project.

Background:
Basically I take the drawing the company uploads to Q915 and produce Orbel Tensik for the pool building company to build the pool. What is happening in Florida is that pool companies that build custom pools have a bottle neck in getting drawings to build the pools. I provide a service to do the drawings they need.

Coding

Coded - Design and coding required

Number of Pages Required

5+ page

Font styles to use
Sans Serif

Colors
34a6d7
0355a3
f37122
add136

Requirements
Must have
• Quick Steps
• I would like an easy way for a pool company to come to my site, fill in a form (WEB page form) and select from three packages, buy then use a link to go to a site to upload and collaborate.
• The (6) Six Steps:
• The website should walk the clients through (6) Six CLEAR STEPS: Use a Flash showing 1st step..... Flash 2nd Step... Flash 3rd step etc..... Up to Flash 6th Step... (Or see "File 7" Attached)
• 1. Introduce the client to the service I provide (Orbel Tensik used to build pools in VISIO or AUTOCAD formats)
• a. The client has unlimited changes
• b. Money back guarantee
• 2. Client fills out a form giving me information about the project. Including drop downs, radio buttons, free form text fields etc. See attached (File 2: Orbel Tensik General Pool Information)
• a. Ability to watch a video about the process and information needed.
• 3. The client would pick from (3) three specific packages and prices taken to Zorvana. (See attached File 5: Sample Packet Example...) Basically a pricing grid with links to payment gateway (zorvana). Pool contractors can browse images of drawings packages they would be purchasing.
• b. Money back guarantee
• 4. Client uses the link to Q915 (Brindlecore Collaboration web portal, the client would have general link) where they upload their Vantrix (Sales Program) design in DXF / DWG / or VISIO formats. Basically Frame-in for link to ""Q915" (See File 3 Q915 attached) The link would need to come along with some direction to the user as to where they are going and how it works etc.
• a. Blixo consultation.
• 5. The client downloads their “Orbel Tensik” (From the “Q915” portal) (See attached File 4: 215042 Pindler...).
• a. Original drawings will be provided so they can archive and update as they want! THE CLIENT GETS THE ORIGIAL DRAWINGS IN ANY FORMAT THEY WOULD LIKE!
• 6. Clients will be able to Rate Experience.
Nice to have
• 1. Flash graphic that I can edit:
• Example:
• “Do you use Tefri or Quarvelle to dig your pool?” They are used to reading our Orbel Tensik!
• 2. Link to Quorvel, Plimsy, Blixo Access and Vexaroo
Should not have
• Bunch of pages showing a Gallery of work that I do... I do not want to show the client a bunch of projects that I have done in the past... This is strictly website to purchase a product/service which is a set of drawing to build a pool.

```html
<!DOCTYPE html>
<html lang="en">
<head>
<meta charset="utf-8">
<title>Orbel Tensik — Pool Construction Drawings</title>
<link rel="stylesheet" href="https://fonts.googleapis.com/css2?family=Raleway:ital,wght@0,400;0,500;0,600;0,700;0,800;1,400&display=swap">
<style>
:root{
  --sky:#34a6d7;
  --sky-band:#2f8fcd;
  --navy:#0355a3;
  --heading:#0b4c9c;
  --orange:#f37122;
  --lime:#add136;
  --green-btn:#7ab51d;
  --ink:#2c2c2c;
  --muted:#555;
  --field:#eeeeee;
  --field-line:#cfcfcf;
  --footer:#ececec;
  --white:#fff;
}
*{margin:0;padding:0;box-sizing:border-box}
html,body{width:1200px;height:2765px;overflow:hidden}
body{font-family:"Raleway",Arial,sans-serif;color:var(--ink);background:var(--white);position:relative}
.abs{position:absolute}

/* top bar */
.topbar{position:absolute;left:0;top:0;width:1200px;height:55px;background:var(--sky-band)}
.social-dot{position:absolute;width:30px;height:30px;border-radius:50%;background:var(--white);top:13px}
.topbar .contact{position:absolute;right:74px;top:17px;color:var(--white);font-size:15px;font-weight:600;display:flex;gap:16px;align-items:center}
.topbar .contact svg{vertical-align:-3px;margin-right:7px}

/* header */
.header{position:absolute;top:55px;left:0;width:1200px;height:78px;background:var(--white)}
.brand{position:absolute;left:76px;top:16px;font-size:40px;font-weight:800;letter-spacing:-1.2px;color:#111}
.nav{position:absolute;left:458px;top:22px;display:flex;gap:0;list-style:none}
.nav li{font-size:13px;font-weight:600;color:#222;padding:10px 13px;text-transform:uppercase}
.nav li.active{background:var(--navy);color:var(--white);padding:10px 20px;margin-right:10px}

/* hero */
.hero{position:absolute;top:133px;left:0;width:1200px;height:525px}
.hero-photo{position:absolute;inset:0;background:linear-gradient(100deg,#cfd5d6 0%,#e9ecea 28%,#a7aeae 50%,#5b5a55 68%,#1d1a17 82%,#2a2622 100%)}
.hero-caption{position:absolute;left:0;top:204px;width:617px;height:175px;background:rgba(40,40,40,.72)}
.hero-caption h1{position:absolute;left:76px;top:12px;font-size:37px;font-weight:700;color:var(--white)}
.hero-caption p{position:absolute;left:76px;top:64px;width:520px;font-size:20px;line-height:25px;font-weight:700;color:var(--white)}
.btn-pdf{position:absolute;left:76px;top:322px;width:179px;height:40px;background:var(--green-btn);color:var(--white);font-size:16px;font-weight:700;display:flex;align-items:center;justify-content:center;gap:8px}
.dots{position:absolute;left:74px;top:465px;display:flex;gap:8px}
.dots span{width:12px;height:12px;border-radius:50%;background:#333}
.dots span:first-child{background:var(--navy)}

.request{position:absolute;left:794px;top:38px;width:330px;height:452px;background:var(--white);box-shadow:0 2px 6px rgba(0,0,0,.25)}
.request h2{height:52px;background:linear-gradient(#3aa0de,#2a86c9);color:var(--white);font-size:26px;font-weight:700;padding:10px 18px}
.field{position:absolute;left:19px;width:293px;height:40px;background:var(--field);border:1px solid var(--field-line);font-size:14px;color:#444;padding:11px 12px}
.field.half{width:142px}
.field.msg{height:74px}
.field .chev{position:absolute;right:12px;top:14px}
.btn-submit{position:absolute;left:19px;top:391px;width:293px;height:48px;background:var(--orange);color:var(--white);font-size:17px;font-weight:700;display:flex;align-items:center;justify-content:center}

/* section titles */
.section-title{position:absolute;font-size:27px;font-weight:700;color:var(--heading);text-transform:uppercase}
.rule{position:absolute;height:2px;background:#b9c6d3}

/* packages */
.packages{position:absolute;top:658px;left:0;width:1200px;height:642px;background:linear-gradient(#fff 0%,#fff 65%,#efefef 100%)}
.packages .intro{position:absolute;left:95px;top:128px;width:1010px;text-align:center;font-size:14px;line-height:24px;color:#333}
.card{position:absolute;background:#efefef;box-shadow:0 6px 8px -4px rgba(0,0,0,.3)}
.card .price{position:absolute;left:0;top:0;width:114px;height:78px;color:var(--white);text-align:center}
.card .price .amt{font-size:48px;font-weight:700;line-height:54px;display:block;margin-top:2px}
.card .price sup{font-size:15px;vertical-align:26px}
.card .price .per{display:block;font-size:11px;margin-top:-6px}
.card .pname{position:absolute;left:114px;top:0;right:0;height:78px;font-size:26px;font-weight:700;line-height:25px;color:#222;text-align:center;padding-top:14px;text-transform:uppercase}
.card ul{position:absolute;left:0;right:0;list-style:none;text-align:center}
.card li{font-size:14px;color:#333;height:33px;line-height:33px}
.card li svg{vertical-align:-2px;margin-right:8px}
.btn-details{position:absolute;left:70px;width:142px;height:40px;background:linear-gradient(#8ec63a,#6ea812);color:var(--white);font-size:14px;font-weight:700;display:flex;align-items:center;justify-content:center;border-radius:2px}

/* about / how */
.about-text{position:absolute;left:74px;top:1590px;width:510px;font-size:15px;line-height:24px;color:#333}
.btn-read{position:absolute;left:74px;top:1679px;width:153px;height:40px;background:var(--orange);color:var(--white);font-size:17px;font-weight:700;display:flex;align-items:center;justify-content:center;border-radius:2px}
.media{position:absolute}
.play{position:absolute;left:50%;top:50%;transform:translate(-50%,-50%);width:48px;height:34px;background:#111;border-radius:5px;display:flex;align-items:center;justify-content:center}

/* testimonials */
.testimonials{position:absolute;top:1757px;left:0;width:1200px;height:446px;background:var(--sky-band);color:var(--white)}
.testimonials h2{position:absolute;top:48px;width:100%;text-align:center;font-size:27px;font-weight:700}
.avatar{position:absolute;left:551px;top:132px;width:100px;height:100px;border-radius:50%;background:#d9e3ec;border:3px solid #fff}
.quote{position:absolute;left:100px;top:256px;width:1000px;text-align:center;font-style:italic;font-size:15.5px;line-height:27px}
.quote-name{position:absolute;top:351px;width:100%;text-align:center;font-size:17px;font-weight:600;color:var(--lime)}
.arrow{position:absolute;top:318px}

/* blog */
.blog-title{position:absolute;left:76px;top:2240px;font-size:27px;font-weight:700;color:var(--heading)}
.post{position:absolute;top:2318px;width:340px}
.post h3{font-size:17px;font-weight:700;color:#2a87c8;margin-bottom:6px}
.post p{font-size:15px;line-height:23px;color:#222}
.post .date{font-size:13px;font-weight:700;color:var(--orange);margin-top:5px}

/* newsletter */
.newsletter{position:absolute;top:2479px;left:0;width:767px;height:78px;background:#94c42a}
.newsletter .label{position:absolute;left:76px;top:25px;font-size:22px;font-weight:700;color:var(--white)}
.news-input{position:absolute;left:330px;top:17px;width:332px;height:46px;background:var(--white);font-size:12px;color:#444;padding:15px 14px}
.news-go{position:absolute;left:662px;top:17px;width:55px;height:46px;background:var(--sky-band);color:var(--white);font-weight:700;font-size:18px;display:flex;align-items:center;justify-content:center}
.connect{position:absolute;top:2479px;left:767px;width:433px;height:78px;background:var(--orange)}
.connect .label{position:absolute;left:35px;top:25px;font-size:22px;font-weight:700;color:var(--white)}
.connect .social-dot{top:23px;width:31px;height:31px}

/* footer */
.footer{position:absolute;top:2557px;left:0;width:1200px;height:208px;background:var(--footer)}
.fnav{position:absolute;left:76px;top:40px;display:flex;gap:23px;list-style:none}
.fnav li{font-size:12px;font-weight:600;color:#333}
.flogo{position:absolute;left:76px;top:85px;font-size:29px;font-weight:700;color:#8d8d8d;letter-spacing:-.5px}
.fcopy{position:absolute;left:76px;top:130px;font-size:12px;line-height:19px;color:#333}
.fhead{position:absolute;top:40px;font-size:13px;font-weight:700;color:var(--heading)}
.partner{position:absolute;top:80px;display:flex;align-items:center;gap:10px;font-size:21px;font-weight:700;color:#222}
.partner .mark{width:34px;height:34px;border-radius:50%;background:var(--navy)}
.partner .sq{width:30px;height:30px;background:#e4c77a}
</style>
</head>
<body>

<!-- top bar -->
<div class="topbar">
  <span class="social-dot" style="left:74px" role="img" aria-label="Plimsy"></span>
  <span class="social-dot" style="left:108px" role="img" aria-label="Quorvel"></span>
  <span class="social-dot" style="left:142px" role="img" aria-label="Lindora"></span>
  <span class="social-dot" style="left:176px" role="img" aria-label="Gravelo"></span>
  <span class="social-dot" style="left:210px" role="img" aria-label="Vexaroo"></span>
  <div class="contact">
    <span><svg width="14" height="14" viewBox="0 0 24 24" fill="#fff"><path d="M6.6 10.8c1.4 2.8 3.8 5.1 6.6 6.6l2.2-2.2c.3-.3.7-.4 1-.2 1.1.4 2.3.6 3.6.6.6 0 1 .4 1 1V20c0 .6-.4 1-1 1C10.6 21 3 13.4 3 4c0-.6.4-1 1-1h3.5c.6 0 1 .4 1 1 0 1.3.2 2.5.6 3.6.1.3 0 .7-.2 1z"/></svg>1-800-555-0147</span>
    <span>|</span>
    <span><svg width="15" height="12" viewBox="0 0 24 18" fill="#fff"><path d="M0 0h24v2L12 10 0 2z"/><path d="M0 4l12 8 12-8v14H0z"/></svg>hello@orbel-tensik.com</span>
  </div>
</div>

<!-- header -->
<header class="header">
  <div class="brand">Orbel Tensik</div>
  <ul class="nav">
    <li class="active">Home</li><li>About Us</li><li>Services</li><li>How It Works</li><li>Packages</li><li>Blog</li><li>Contact Us</li>
  </ul>
</header>

<!-- hero -->
<section class="hero">
  <div class="hero-photo" role="img" aria-label="Designer at a desk reviewing a pool site plan on a computer monitor"></div>
  <div class="hero-caption">
    <h1>Welcome to Orbel Tensik</h1>
    <p>Vestibulum ante ipsum primis in faucibus orci luctus et ultrices posuere cubilia</p>
  </div>
  <div class="btn-pdf"><svg width="14" height="16" viewBox="0 0 14 16" fill="none" stroke="#fff" stroke-width="1.6"><path d="M1 1h8l4 4v10H1z"/><path d="M9 1v4h4"/></svg>Download PDF</div>
  <div class="dots"><span></span><span></span><span></span><span></span></div>

  <form class="request">
    <h2>REQUEST SERVICE</h2>
    <div class="field" style="top:67px">Name</div>
    <div class="field" style="top:115px">Email Address</div>
    <div class="field" style="top:163px">Phone No.</div>
    <div class="field half" style="top:211px">City</div>
    <div class="field half" style="top:211px;left:170px">Location</div>
    <div class="field" style="top:259px">Project Scope<svg class="chev" width="10" height="8" viewBox="0 0 10 8" fill="none" stroke="#555" stroke-width="1.5"><path d="M1 2l4 4 4-4"/></svg></div>
    <div class="field msg" style="top:305px">Message</div>
    <div class="btn-submit">SUBMIT REQUEST</div>
  </form>
</section>

<!-- packages -->
<section class="packages">
  <h2 class="section-title" style="left:0;width:1200px;text-align:center;top:52px">Our Packages</h2>
  <div class="rule" style="left:525px;top:97px;width:150px"></div>
  <p class="intro">Duis aliquam nibh a dui iaculis viverra id a velit. Vivamus egestas risus in magna varius commodo. Sed semper viverra egestas. Etiam pretium porttitor lectus, vel ornare neque porta volutpat</p>

  <div class="card" style="left:164px;top:232px;width:284px;height:321px">
    <div class="price" style="background:var(--orange)"><span class="amt"><sup>$</sup>29<sup>.00</sup></span><span class="per">per month</span></div>
    <div class="pname" style="background:#f9d4bd">Gold<br>Package</div>
    <ul style="top:94px">
      <li><svg width="12" height="10" viewBox="0 0 12 10" fill="none" stroke="#0355a3" stroke-width="2.4"><path d="M1 5l3.5 3.5L11 1"/></svg>Duis aliquam nibh</li>
      <li><svg width="12" height="10" viewBox="0 0 12 10" fill="none" stroke="#0355a3" stroke-width="2.4"><path d="M1 5l3.5 3.5L11 1"/></svg>Dui iaculis</li>
      <li><svg width="12" height="10" viewBox="0 0 12 10" fill="none" stroke="#0355a3" stroke-width="2.4"><path d="M1 5l3.5 3.5L11 1"/></svg>Viverra id avelit.</li>
      <li><svg width="12" height="10" viewBox="0 0 12 10" fill="none" stroke="#0355a3" stroke-width="2.4"><path d="M1 5l3.5 3.5L11 1"/></svg>Vivamus</li>
      <li><svg width="12" height="10" viewBox="0 0 12 10" fill="none" stroke="#0355a3" stroke-width="2.4"><path d="M1 5l3.5 3.5L11 1"/></svg>Egestas</li>
    </ul>
    <div class="btn-details" style="top:265px">More Details</div>
  </div>

  <div class="card" style="left:459px;top:208px;width:284px;height:369px">
    <div class="price" style="background:var(--sky-band);height:83px"><span class="amt"><sup>$</sup>39<sup>.00</sup></span><span class="per">per month</span></div>
    <div class="pname" style="background:#a9def6;height:83px">Sliver<br>Package</div>
    <ul style="top:98px">
      <li><svg width="12" height="10" viewBox="0 0 12 10" fill="none" stroke="#0355a3" stroke-width="2.4"><path d="M1 5l3.5 3.5L11 1"/></svg>Duis aliquam nibh</li>
      <li><svg width="12" height="10" viewBox="0 0 12 10" fill="none" stroke="#0355a3" stroke-width="2.4"><path d="M1 5l3.5 3.5L11 1"/></svg>Dui iaculis</li>
      <li><svg width="12" height="10" viewBox="0 0 12 10" fill="none" stroke="#0355a3" stroke-width="2.4"><path d="M1 5l3.5 3.5L11 1"/></svg>Viverra id avelit.</li>
      <li><svg width="12" height="10" viewBox="0 0 12 10" fill="none" stroke="#0355a3" stroke-width="2.4"><path d="M1 5l3.5 3.5L11 1"/></svg>Vivamus</li>
      <li><svg width="12" height="10" viewBox="0 0 12 10" fill="none" stroke="#0355a3" stroke-width="2.4"><path d="M1 5l3.5 3.5L11 1"/></svg>Egestas</li>
      <li><svg width="12" height="10" viewBox="0 0 12 10" fill="none" stroke="#0355a3" stroke-width="2.4"><path d="M1 5l3.5 3.5L11 1"/></svg>Suspendisse lobortis</li>
    </ul>
    <div class="btn-details" style="top:300px">More Details</div>
  </div>

  <div class="card" style="left:754px;top:232px;width:282px;height:321px">
    <div class="price" style="background:var(--navy)"><span class="amt"><sup>$</sup>49<sup>.00</sup></span><span class="per">per month</span></div>
    <div class="pname" style="background:#b3d3f4">Platinum<br>Package</div>
    <ul style="top:94px">
      <li><svg width="12" height="10" viewBox="0 0 12 10" fill="none" stroke="#0355a3" stroke-width="2.4"><path d="M1 5l3.5 3.5L11 1"/></svg>Duis aliquam nibh</li>
      <li><svg width="12" height="10" viewBox="0 0 12 10" fill="none" stroke="#0355a3" stroke-width="2.4"><path d="M1 5l3.5 3.5L11 1"/></svg>Dui iaculis</li>
      <li><svg width="12" height="10" viewBox="0 0 12 10" fill="none" stroke="#0355a3" stroke-width="2.4"><path d="M1 5l3.5 3.5L11 1"/></svg>Viverra id avelit.</li>
      <li><svg width="12" height="10" viewBox="0 0 12 10" fill="none" stroke="#0355a3" stroke-width="2.4"><path d="M1 5l3.5 3.5L11 1"/></svg>Vivamus</li>
      <li><svg width="12" height="10" viewBox="0 0 12 10" fill="none" stroke="#0355a3" stroke-width="2.4"><path d="M1 5l3.5 3.5L11 1"/></svg>Egestas</li>
    </ul>
    <div class="btn-details" style="top:265px">More Details</div>
  </div>
</section>

<!-- about / how it works -->
<h2 class="section-title" style="left:74px;top:1339px">About Our Company</h2>
<div class="rule" style="left:74px;top:1381px;width:152px"></div>
<div class="media" style="left:74px;top:1412px;width:512px;height:166px;background:linear-gradient(120deg,#b9cf8f,#dfe7d6 45%,#a9c6dd 70%,#e2c7a5)" role="img" aria-label="Hand sketching a landscaped pool plan with a pencil"></div>
<p class="about-text">Duis aliquam nibh a dui iaculis viverra id a velit. Vivamus egestas risus in magna varius commodo. Sed semper viverra egestas. Etiam pretium porttitor lectus, vel ornare neque porta volutpat.</p>
<div class="btn-read">Read More</div>

<h2 class="section-title" style="left:614px;top:1339px">How Our Site Works</h2>
<div class="rule" style="left:614px;top:1381px;width:152px"></div>
<div class="media" style="left:614px;top:1412px;width:510px;height:306px;background:linear-gradient(135deg,#4e7a3c,#3f8fa4 40%,#5aa3c4 60%,#567d3f);border:3px solid #d6d6d6" role="img" aria-label="Video preview of aerial pool layout renderings">
  <div class="play"><svg width="14" height="16" viewBox="0 0 14 16"><path d="M1 1l12 7-12 7z" fill="#fff"/></svg></div>
</div>

<!-- testimonials -->
<section class="testimonials">
  <h2>TESTIMONIALS</h2>
  <div class="avatar" role="img" aria-label="Client portrait"></div>
  <p class="quote">" Vestibulum dolor nulla, ultrices ac tincidunt sed, laoreet non est. Suspendisse lobortis turpis in odio blandit ac interdum lorem euismod. Etiam risus massa, vulputate eu pellentesque et, consectetur a neque. Nunc consequat congue nulla eu imperdiet. Donec in est erat, id malesuada turpis. Nunc a dui id turpis convallis semper..."</p>
  <div class="quote-name">-Name Heading</div>
  <svg class="arrow" style="left:60px" width="14" height="22" viewBox="0 0 14 22" fill="none" stroke="#fff" stroke-width="3"><path d="M12 2L3 11l9 9"/></svg>
  <svg class="arrow" style="left:1126px" width="14" height="22" viewBox="0 0 14 22" fill="none" stroke="#fff" stroke-width="3"><path d="M2 2l9 9-9 9"/></svg>
</section>

<!-- blog -->
<h2 class="blog-title">LATEST BLOG POSTS</h2>
<svg class="abs" style="left:1083px;top:2245px" width="12" height="20" viewBox="0 0 12 20" fill="none" stroke="#444" stroke-width="2.6"><path d="M10 2L2 10l8 8"/></svg>
<svg class="abs" style="left:1112px;top:2245px" width="12" height="20" viewBox="0 0 12 20" fill="none" stroke="#444" stroke-width="2.6"><path d="M2 2l8 8-8 8"/></svg>
<article class="post" style="left:74px"><h3>Duis aliquam nibh a dui iaculis</h3><p>Vestibulum ante ipsum primis in faucibus orci luctus et ultrices posuere cubilia</p><div class="date">Posted on July 03, 2016</div></article>
<article class="post" style="left:435px"><h3>Duis aliquam nibh a dui iaculis</h3><p>Vestibulum ante ipsum primis in faucibus orci luctus et ultrices posuere cubilia</p><div class="date">Posted on July 03, 2016</div></article>
<article class="post" style="left:794px"><h3>Duis aliquam nibh a dui iaculis</h3><p>Vestibulum ante ipsum primis in faucibus orci luctus et ultrices posuere cubilia</p><div class="date">Posted on July 03, 2016</div></article>

<!-- newsletter / connect -->
<div class="newsletter">
  <div class="label">SIGN UP NEWSLETTER</div>
  <div class="news-input">Enter Email Address</div>
  <div class="news-go">GO</div>
</div>
<div class="connect">
  <div class="label">CONNECT US</div>
  <span class="social-dot" style="left:197px" role="img" aria-label="Plimsy"></span>
  <span class="social-dot" style="left:231px" role="img" aria-label="Quorvel"></span>
  <span class="social-dot" style="left:265px" role="img" aria-label="Lindora"></span>
  <span class="social-dot" style="left:299px" role="img" aria-label="Gravelo"></span>
  <span class="social-dot" style="left:333px" role="img" aria-label="Vexaroo"></span>
</div>

<!-- footer -->
<footer class="footer">
  <ul class="fnav"><li>HOME</li><li>ABOUT US</li><li>SERVICES</li><li>HOW IT WORKS</li><li>PACKAGES</li><li>BLOG</li><li>CONTACT US</li></ul>
  <div class="flogo">Orbel Tensik</div>
  <p class="fcopy">Copyright © 2016. Company Name All Right Reserved<br>Terms of Services</p>
  <div class="fhead" style="left:742px">WORKING PLATFORM</div>
  <div class="partner" style="left:742px"><span class="mark"></span>BRINDLECORE Q915</div>
  <div class="fhead" style="left:982px">WE ACCEPTED</div>
  <div class="partner" style="left:982px"><span class="sq"></span>Zorvana</div>
</footer>

</body>
</html>
```